Tights Color Chart

We Need for a Webshop 3 or 4 different Color Charts to see the Colors of the Tights.

1 Color Chart only with this Colors: black/schwarz, white/weiss,
naturel/natur.

The other 3 or 4 Charts up to your Design!

Total 54 Colors.

The Language must be in English and German.
Each single Color Chart should have rounded Corners see attachment.

Thank you in advance
BEN

Target Market(s)

Woman, Webshop

Requirements
Must have
• the right Colors, English and German, for the Webshop

```html
<!DOCTYPE html>
<html lang="en">
<head>
<meta charset="utf-8">
<title>Tights Color Chart</title>
<link rel="stylesheet" href="https://fonts.googleapis.com/css2?family=Noto+Sans:wght@400;700&display=swap">
<style>
  :root {
    --page-bg: #f2f2f2;
    --ink: #000000;
  }
  * { margin: 0; padding: 0; box-sizing: border-box; }
  html, body { width: 842px; height: 1200px; overflow: hidden; }
  body {
    background: var(--page-bg);
    font-family: "Noto Sans", sans-serif;
    color: var(--ink);
    position: relative;
  }
  .color-chart {
    position: absolute;
    left: 117px;
    top: 91px;
    display: grid;
    grid-template-columns: repeat(6, 87px);
    grid-template-rows: 97px 101px 102px 96px 101px 106px 96px 101px 100px;
    column-gap: 18.8px;
  }
  .shade { position: relative; width: 87px; }
  .shade__swatch {
    width: 87px;
    height: 58px;
    border-radius: 14px;
    background: linear-gradient(90deg, var(--a), var(--b));
  }
  .shade__label {
    position: absolute;
    left: -20px;
    width: 127px;
    top: 64px;
    text-align: center;
    line-height: 13px;
    letter-spacing: -0.2px;
  }
  .shade__en { display: block; font-weight: 700; font-size: 11px; }
  .shade__de { display: block; font-weight: 400; font-size: 10.5px; }
  .chart-title,
  .chart-font {
    position: absolute;
    left: 0; right: 0;
    text-align: center;
    font-weight: 700;
    font-size: 23px;
    letter-spacing: 0.3px;
  }
  .chart-title { top: 1056px; }
  .chart-font { top: 1109px; }
</style>
</head>
<body>
<main class="color-chart">
  <div class="shade" style="--a:#9f8fba;--b:#d4b8e8"><div class="shade__swatch"></div><p class="shade__label"><span class="shade__en">lila</span><span class="shade__de">lila</span></p></div>
  <div class="shade" style="--a:#6b5a96;--b:#9b74b8"><div class="shade__swatch"></div><p class="shade__label"><span class="shade__en">iris</span><span class="shade__de">iris</span></p></div>
  <div class="shade" style="--a:#6e3f7e;--b:#9a55a0"><div class="shade__swatch"></div><p class="shade__label"><span class="shade__en">azalea</span><span class="shade__de">azalea</span></p></div>
  <div class="shade" style="--a:#6a2f55;--b:#86416a"><div class="shade__swatch"></div><p class="shade__label"><span class="shade__en">mulberry</span><span class="shade__de">maulbeere</span></p></div>
  <div class="shade" style="--a:#7a2a5c;--b:#a84380"><div class="shade__swatch"></div><p class="shade__label"><span class="shade__en">fuchsia</span><span class="shade__de">fuchsia</span></p></div>
  <div class="shade" style="--a:#8f3f6a;--b:#c25a8e"><div class="shade__swatch"></div><p class="shade__label"><span class="shade__en">lavende</span><span class="shade__de">lavendel</span></p></div>

  <div class="shade" style="--a:#a8458e;--b:#db5eb0"><div class="shade__swatch"></div><p class="shade__label"><span class="shade__en">crocus</span><span class="shade__de">krokus</span></p></div>
  <div class="shade" style="--a:#b8b2b6;--b:#fff2f6"><div class="shade__swatch"></div><p class="shade__label"><span class="shade__en">baby pink</span><span class="shade__de">baby rosa</span></p></div>
  <div class="shade" style="--a:#a8909c;--b:#f0d4de"><div class="shade__swatch"></div><p class="shade__label"><span class="shade__en">rose</span><span class="shade__de">hellrosa</span></p></div>
  <div class="shade" style="--a:#c0789e;--b:#f8a8d0"><div class="shade__swatch"></div><p class="shade__label"><span class="shade__en">pink</span><span class="shade__de">rosa</span></p></div>
  <div class="shade" style="--a:#b06a98;--b:#e690b8"><div class="shade__swatch"></div><p class="shade__label"><span class="shade__en">orchidea</span><span class="shade__de">orchidea</span></p></div>
  <div class="shade" style="--a:#a83050;--b:#e0567a"><div class="shade__swatch"></div><p class="shade__label"><span class="shade__en">raspberry</span><span class="shade__de">himbeer</span></p></div>

  <div class="shade" style="--a:#a83a48;--b:#e05a62"><div class="shade__swatch"></div><p class="shade__label"><span class="shade__en">sorbet</span><span class="shade__de">sorbet</span></p></div>
  <div class="shade" style="--a:#8c2e44;--b:#b24c5c"><div class="shade__swatch"></div><p class="shade__label"><span class="shade__en">lipstic</span><span class="shade__de">rot</span></p></div>
  <div class="shade" style="--a:#8c302e;--b:#c24c48"><div class="shade__swatch"></div><p class="shade__label"><span class="shade__en">rosso</span><span class="shade__de">rosso</span></p></div>
  <div class="shade" style="--a:#a8622a;--b:#e8883a"><div class="shade__swatch"></div><p class="shade__label"><span class="shade__en">orange</span><span class="shade__de">orange</span></p></div>
  <div class="shade" style="--a:#a86a6a;--b:#e09a8e"><div class="shade__swatch"></div><p class="shade__label"><span class="shade__en">salmon</span><span class="shade__de">lachs</span></p></div>
  <div class="shade" style="--a:#8c7262;--b:#cca494"><div class="shade__swatch"></div><p class="shade__label"><span class="shade__en">naturel</span><span class="shade__de">natur</span></p></div>

  <div class="shade" style="--a:#8c644a;--b:#b88c6a"><div class="shade__swatch"></div><p class="shade__label"><span class="shade__en">beige</span><span class="shade__de">beige</span></p></div>
  <div class="shade" style="--a:#6a5048;--b:#927462"><div class="shade__swatch"></div><p class="shade__label"><span class="shade__en">nugat</span><span class="shade__de">nougat</span></p></div>
  <div class="shade" style="--a:#6e5656;--b:#a08080"><div class="shade__swatch"></div><p class="shade__label"><span class="shade__en">cacao</span><span class="shade__de">kakao</span></p></div>
  <div class="shade" style="--a:#9a9a9a;--b:#e6e6e4"><div class="shade__swatch"></div><p class="shade__label"><span class="shade__en">ash</span><span class="shade__de">asche</span></p></div>
  <div class="shade" style="--a:#b4b2aa;--b:#f6f4ec"><div class="shade__swatch"></div><p class="shade__label"><span class="shade__en">perle</span><span class="shade__de">perle</span></p></div>
  <div class="shade" style="--a:#bcbcb8;--b:#f8fcf4"><div class="shade__swatch"></div><p class="shade__label"><span class="shade__en">ecru</span><span class="shade__de">ecru</span></p></div>

  <div class="shade" style="--a:#c0c0b8;--b:#fffff4"><div class="shade__swatch"></div><p class="shade__label"><span class="shade__en">kalina</span><span class="shade__de">kalina</span></p></div>
  <div class="shade" style="--a:#b8b8aa;--b:#f6f8ea"><div class="shade__swatch"></div><p class="shade__label"><span class="shade__en">cream</span><span class="shade__de">creme</span></p></div>
  <div class="shade" style="--a:#b8b8b8;--b:#ffffff"><div class="shade__swatch"></div><p class="shade__label"><span class="shade__en">white</span><span class="shade__de">weiss</span></p></div>
  <div class="shade" style="--a:#6a2e54;--b:#8e4470"><div class="shade__swatch"></div><p class="shade__label"><span class="shade__en">violet</span><span class="shade__de">violett</span></p></div>
  <div class="shade" style="--a:#6a3e52;--b:#926074"><div class="shade__swatch"></div><p class="shade__label"><span class="shade__en">prugna</span><span class="shade__de">pflaume</span></p></div>
  <div class="shade" style="--a:#5e3e58;--b:#8a6078"><div class="shade__swatch"></div><p class="shade__label"><span class="shade__en">berry</span><span class="shade__de">beerch</span></p></div>

  <div class="shade" style="--a:#5a3c3c;--b:#7e5652"><div class="shade__swatch"></div><p class="shade__label"><span class="shade__en">bronzo</span><span class="shade__de">bronze</span></p></div>
  <div class="shade" style="--a:#46462a;--b:#626038"><div class="shade__swatch"></div><p class="shade__label"><span class="shade__en">olive</span><span class="shade__de">olive</span></p></div>
  <div class="shade" style="--a:#a8b46a;--b:#eafca4"><div class="shade__swatch"></div><p class="shade__label"><span class="shade__en">kiwi</span><span class="shade__de">kiwi</span></p></div>
  <div class="shade" style="--a:#5aa468;--b:#88e088"><div class="shade__swatch"></div><p class="shade__label"><span class="shade__en">verde</span><span class="shade__de">grün</span></p></div>
  <div class="shade" style="--a:#2e7a46;--b:#4cb05a"><div class="shade__swatch"></div><p class="shade__label"><span class="shade__en">grass</span><span class="shade__de">grassgrün</span></p></div>
  <div class="shade" style="--a:#6aae96;--b:#aaf0dc"><div class="shade__swatch"></div><p class="shade__label"><span class="shade__en">aquamarina</span><span class="shade__de">aquamarina</span></p></div>

  <div class="shade" style="--a:#1e8c7a;--b:#38d2c0"><div class="shade__swatch"></div><p class="shade__label"><span class="shade__en">lagoon</span><span class="shade__de">lagune</span></p></div>
  <div class="shade" style="--a:#3a9a9a;--b:#72dcd8"><div class="shade__swatch"></div><p class="shade__label"><span class="shade__en">lazur</span><span class="shade__de">lazur</span></p></div>
  <div class="shade" style="--a:#1a9aa2;--b:#32d0d8"><div class="shade__swatch"></div><p class="shade__label"><span class="shade__en">turquoise</span><span class="shade__de">türkis</span></p></div>
  <div class="shade" style="--a:#7a96b8;--b:#bcdaf4"><div class="shade__swatch"></div><p class="shade__label"><span class="shade__en">blue</span><span class="shade__de">blau</span></p></div>
  <div class="shade" style="--a:#3e3e66;--b:#5e5a8a"><div class="shade__swatch"></div><p class="shade__label"><span class="shade__en">baby blue</span><span class="shade__de">baby blau</span></p></div>
  <div class="shade" style="--a:#3a4e66;--b:#5a7a96"><div class="shade__swatch"></div><p class="shade__label"><span class="shade__en">jeans</span><span class="shade__de">jeans</span></p></div>

  <div class="shade" style="--a:#32303e;--b:#4a4658"><div class="shade__swatch"></div><p class="shade__label"><span class="shade__en">ocean</span><span class="shade__de">ozean</span></p></div>
  <div class="shade" style="--a:#2e3044;--b:#42465e"><div class="shade__swatch"></div><p class="shade__label"><span class="shade__en">night</span><span class="shade__de">nacht</span></p></div>
  <div class="shade" style="--a:#3a2c48;--b:#52406a"><div class="shade__swatch"></div><p class="shade__label"><span class="shade__en">blu marino</span><span class="shade__de">blu marino</span></p></div>
  <div class="shade" style="--a:#463a5e;--b:#625680"><div class="shade__swatch"></div><p class="shade__label"><span class="shade__en">blu marino melange</span><span class="shade__de">blu marino melange</span></p></div>
  <div class="shade" style="--a:#342836;--b:#4a3a4e"><div class="shade__swatch"></div><p class="shade__label"><span class="shade__en">denim</span><span class="shade__de">denim</span></p></div>
  <div class="shade" style="--a:#444848;--b:#5e6460"><div class="shade__swatch"></div><p class="shade__label"><span class="shade__en">silver</span><span class="shade__de">silber</span></p></div>

  <div class="shade" style="--a:#6e5a68;--b:#92808e"><div class="shade__swatch"></div><p class="shade__label"><span class="shade__en">steel</span><span class="shade__de">stahl</span></p></div>
  <div class="shade" style="--a:#52424a;--b:#6e5c62"><div class="shade__swatch"></div><p class="shade__label"><span class="shade__en">gray</span><span class="shade__de">grau</span></p></div>
  <div class="shade" style="--a:#4a4044;--b:#665a5c"><div class="shade__swatch"></div><p class="shade__label"><span class="shade__en">graphite</span><span class="shade__de">graphit</span></p></div>
  <div class="shade" style="--a:#3e3e3e;--b:#525452"><div class="shade__swatch"></div><p class="shade__label"><span class="shade__en">smoke</span><span class="shade__de">rauch</span></p></div>
  <div class="shade" style="--a:#363434;--b:#4a4848"><div class="shade__swatch"></div><p class="shade__label"><span class="shade__en">nero</span><span class="shade__de">schwarz</span></p></div>
  <div class="shade" style="--a:#323232;--b:#484646"><div class="shade__swatch"></div><p class="shade__label"><span class="shade__en">nero melange</span><span class="shade__de">schwarz melange</span></p></div>
</main>

<h1 class="chart-title">TIGHTS COLOR CHART</h1>
<p class="chart-font">FONT: LUMIRA SANS</p>
</body>
</html>
```